Maple Syrup Bottle (front) Label design

I need label design for a 16fl OZ rectangular bottle of maple syrup with the usable dimensions of: Front: 4" x 2" and the back area for "ingredient specifications" of: 6" x 2". The maple syrup product comes from our own farm and is a quality product. The technical name/class of the syrup is: Grade A / AMBER
Updates

I can’t seem to find a way to upload a photo of the maple syrup bottle, but the front dimensions are clearly written on bottle description. Again: 4.5” by 2.25”

I have tried to upload the photo of the maple syrup bottle several times, and it seems (from my side) that it is successful. But I can never find it and the artists cannot find it either. Not sure what to do.

I have tried several times to add a photo of maple bottle, but it never shows up

This seems to be a futile exercise

I would like to post some images of the actual quill Hollow (not the one on Fendix, though!
But I can’t get back to the page that allows that to happen. Please advise!

Somebody PLEASE ask PW management to make it possible for me to upload more images! The "add photos" etc. just disappears from anywhere.

Target Market(s)

High-end food stores

Industry/Entity Type

Maple syrup retail industry

Other font styles liked:
• I don't know, and welcome suggestions

Colors

Designer to choose colors to be used in the design.

Requirements
Must have
• Name of Farm: Quill Hollow Maple
Nice to have
• The label can be "minimalist" and elegant. There is already a Maple leaf glass relief on the top of front of the bottle.
Should not have
• and NOT include farm buildings with steam coming out the chimney, etc.

```html
<!DOCTYPE html>
<html lang="en">
<head>
<meta charset="utf-8">
<title>Quill Hollow Maple – Maple Syrup Label</title>
<link rel="stylesheet" href="https://fonts.googleapis.com/css2?family=Jost:ital,wght@0,400;0,500;0,600;0,700;1,600;1,700&display=swap">
<style>
  :root {
    --page: #ffffff;
    --label: #e49b67;
    --ink: #b4523a;
    --leaf: #d47d56;
  }
  * { margin: 0; padding: 0; box-sizing: border-box; }
  html, body {
    width: 1200px;
    height: 751px;
    overflow: hidden;
    background: var(--page);
  }
  .canvas {
    position: relative;
    width: 1200px;
    height: 751px;
    background: var(--page);
  }
  .label {
    position: absolute;
    left: 434px;
    top: 60px;
    width: 332px;
    height: 626px;
    background: var(--label);
    color: var(--ink);
    font-family: "Jost", "Futura", sans-serif;
    text-align: center;
  }
  .label > * {
    position: absolute;
    left: 0;
    width: 100%;
  }
  .farm-name {
    top: 64px;
    font-size: 19px;
    font-weight: 700;
    letter-spacing: 1.6px;
  }
  .purity-mark {
    top: 116px;
    height: 80px;
  }
  .purity-mark .leaf-area {
    position: absolute;
    left: 128px;
    top: 0;
    width: 76px;
    height: 64px;
    border-radius: 38px 38px 30px 30px;
    background: var(--leaf);
    opacity: 0.75;
  }
  .purity-mark .leaf-stem {
    position: absolute;
    left: 165px;
    top: 60px;
    width: 2px;
    height: 20px;
    background: var(--leaf);
  }
  .purity-mark .purity-text {
    position: absolute;
    left: 0;
    width: 100%;
    top: 26px;
    font-size: 16px;
    font-weight: 700;
    line-height: 15px;
    letter-spacing: 1.5px;
    color: var(--ink);
    opacity: 0.9;
  }
  .product-name {
    top: 208px;
    font-size: 71px;
    font-weight: 400;
    line-height: 70px;
    letter-spacing: 7px;
    padding-left: 7px;
  }
  .quality-seal {
    top: 376px;
    left: 127px;
    width: 78px;
    height: 78px;
  }
  .grade {
    top: 470px;
    font-size: 15px;
    font-weight: 700;
    font-style: italic;
    letter-spacing: 1.4px;
  }
  .variety {
    top: 510px;
    font-size: 14px;
    font-weight: 500;
    letter-spacing: 1.6px;
  }
  .volume {
    top: 558px;
    font-size: 15px;
    font-weight: 700;
    font-style: italic;
    letter-spacing: 1.5px;
  }
</style>
</head>
<body>
<main class="canvas">
  <section class="label" aria-label="Maple syrup bottle front label">
    <p class="farm-name">Quill Hollow Maple</p>

    <div class="purity-mark">
      <div class="leaf-area" role="img" aria-label="Soft maple leaf shape behind the purity note"></div>
      <div class="leaf-stem"></div>
      <p class="purity-text">100%<br>PURE</p>
    </div>

    <h1 class="product-name">MAPLE<br>SYRUP</h1>

    <svg class="quality-seal" viewBox="0 0 78 78" aria-label="Quality product 2023">
      <defs>
        <path id="seal-ring" d="M39,39 m-31,0 a31,31 0 1,1 62,0 a31,31 0 1,1 -62,0"/>
      </defs>
      <text font-family="Jost, sans-serif" font-size="11" font-weight="500" fill="var(--ink)" letter-spacing="2.2">
        <textPath href="#seal-ring" startOffset="2%">QUALITY PRODUCT</textPath>
      </text>
      <text x="39" y="44" text-anchor="middle" font-family="Jost, sans-serif" font-size="14" font-weight="600" fill="var(--ink)" letter-spacing="1">2023</text>
    </svg>

    <p class="grade">Grade A / AMBER</p>
    <p class="variety">ORIGINAL MAPLE SYRUP</p>
    <p class="volume">16 fl oz</p>
  </section>
</main>
</body>
</html>
```